Calbrook Partners needs new business cards

Please refer to brief for logo design and use design #2447418. I would like to see a few concepts as I may not always go to print with full colour backing. At front of card I'd like to include staff name, company name and contact details. At back of card I'd like to include a tag line and list of services.
Updates

Reason: I have extended the deadline because I'm still hoping to receive the ideal business card for Calbrook Partners

Target Market(s)

Middle to senior executives within corporate sector. Top end of town eg, telcos, banks, large hospitals, technology companies.

Requirements
Must have
• Design #2447418 logo and colours
Nice to have
• the back of the card can be as creative as the concept you already submitted, which was quite nice.
Should not have
• Not too busy or cluttered, bearing in mind original logo brief

```html
<!DOCTYPE html>
<html lang="en">
<head>
<meta charset="utf-8">
<title>Calbrook Partners – Business Card</title>
<link rel="stylesheet" href="https://fonts.googleapis.com/css2?family=Josefin+Sans:wght@300;400;600&display=swap">
<style>
  :root {
    --backdrop: #3b322d;
    --card: #ffffff;
    --navy: #2c2a6d;
    --sky: #2b8fd4;
    --shadow: rgba(0, 0, 0, 0.45);
  }
  html, body {
    margin: 0;
    padding: 0;
    width: 1200px;
    height: 1000px;
    overflow: hidden;
    background: var(--backdrop);
  }
  .canvas {
    position: relative;
    width: 1200px;
    height: 1000px;
    display: flex;
    align-items: center;
    justify-content: center;
  }
  .business-card {
    position: relative;
    width: 840px;
    height: 480px;
    background: var(--card);
    box-shadow: 0 14px 30px var(--shadow);
    font-family: "Josefin Sans", sans-serif;
    color: var(--navy);
  }
  .brand {
    position: absolute;
    left: 200px;
    top: 118px;
    display: flex;
    align-items: center;
    gap: 18px;
  }
  .brand-dot {
    width: 54px;
    height: 54px;
  }
  .brand-name {
    font-size: 50px;
    font-weight: 600;
    color: var(--navy);
    letter-spacing: 0.5px;
    line-height: 1;
    padding-top: 6px;
  }
  .staff-name {
    position: absolute;
    left: 0;
    right: 0;
    top: 228px;
    text-align: center;
    font-size: 44px;
    font-weight: 300;
    letter-spacing: 6px;
    color: var(--navy);
    margin: 0;
  }
  .contact-list {
    position: absolute;
    left: 46px;
    right: 40px;
    bottom: 66px;
    display: flex;
    justify-content: space-between;
    margin: 0;
    padding: 0;
    list-style: none;
  }
  .contact-item {
    display: flex;
    flex-direction: column;
    gap: 6px;
  }
  .contact-label {
    font-size: 14px;
    font-weight: 400;
    color: var(--sky);
    letter-spacing: 0.5px;
  }
  .contact-value {
    font-size: 15px;
    font-weight: 400;
    color: var(--navy);
    letter-spacing: 1px;
  }
</style>
</head>
<body>
  <main class="canvas">
    <article class="business-card">
      <div class="brand">
        <svg class="brand-dot" viewBox="0 0 54 54" aria-hidden="true">
          <circle cx="27" cy="27" r="24" fill="#2b8fd4"/>
        </svg>
        <span class="brand-name">Calbrook Partners</span>
      </div>

      <h1 class="staff-name">Daniel Reyes</h1>

      <ul class="contact-list">
        <li class="contact-item">
          <span class="contact-label">Phone:</span>
          <span class="contact-value">555 555 555</span>
        </li>
        <li class="contact-item">
          <span class="contact-label">Web:</span>
          <span class="contact-value">www.yourweb.com</span>
        </li>
        <li class="contact-item">
          <span class="contact-label">Email:</span>
          <span class="contact-value">danielreyes@email.com</span>
        </li>
        <li class="contact-item">
          <span class="contact-label">Address:</span>
          <span class="contact-value">1 Harbour St Los Angeles, CA9012</span>
        </li>
      </ul>
    </article>
  </main>
</body>
</html>
```